new KVR one page flyer

We need a 1 page A4 size flyer (need it asap please) that describes on 1 page with art work and using photos the services we provide. I have included some examples of old previous flyers from our other (seperate divisions of the business) I have named a photo called (photo for top of design) however you do your design this photo needs to be the star of the page by either having it at the top or bottom of the page please and we usually like this photo to be in greyscale colour.
we do like greyscale designs but are open to see what you come up with as a whole page of grey white and black might not suit.

Needs to list the following

Services include:
Over size loads / Hot Shot Loads
Heavy Vehicle Recovery services
Potable Water Deliveries
Road Building / Maintenance
Earthworks
Sand & Metal Supply & Cartage
Road Train Tippers
Road Train Tankers
Road Train Flat Tops
Drop Deck Trailers
Mine site accredited equipment & Operators.

We offer a large rage of services not listed so call us today for a personalised quote to suit your needs.

To go on the bottom of the page our contact details are

KVR Pty Ltd
Depot: Lot 514, Banksia Flats Track Coober Pedy
Mobile: 047 216 9381
email: darren@kestrelvaleroadworks.com.au

Target Market(s)

new clients

Colors

Designer to choose colors to be used in the design.

Requirements
Must have
• our services listed
Nice to have
• stand out designs

```html
<!DOCTYPE html>
<html lang="en">
<head>
<meta charset="utf-8">
<title>KVR Services Flyer</title>
<link rel="stylesheet" href="https://fonts.googleapis.com/css2?family=Krona+One&family=Montserrat:wght@400;500;600;700;800&display=swap">
<style>
  :root {
    --backdrop: #a6a6a6;
    --paper: #ffffff;
    --charcoal: #3a3a3c;
    --charcoal-deep: #2c2c2e;
    --gold: #a5773a;
    --gold-light: #c4954f;
    --ink: #2b2b2b;
  }
  * { margin: 0; padding: 0; box-sizing: border-box; }
  html, body {
    width: 1200px; height: 1200px; overflow: hidden;
    background: var(--backdrop);
    font-family: "Montserrat", sans-serif;
  }
  .flyer {
    position: absolute; left: 200px; top: 34px;
    width: 800px; height: 1131px;
    background: var(--paper);
    overflow: hidden;
    box-shadow: 0 10px 30px rgba(0,0,0,.25);
  }
  .flyer-art { position: absolute; inset: 0; }
  .brand-mark {
    position: absolute; top: 36px; left: 300px;
    font-family: "Montserrat", sans-serif; font-weight: 800;
    font-size: 84px; letter-spacing: 4px; color: var(--charcoal);
  }
  .headline {
    position: absolute; left: 36px; top: 612px;
    font-family: "Krona One", sans-serif; font-weight: 400;
    color: #fff; font-size: 32px; line-height: 1.2; letter-spacing: 1px;
  }
  .services { position: absolute; left: 50px; top: 772px; }
  .services-title {
    font-weight: 800; font-size: 24px; line-height: 28px; color: var(--ink); letter-spacing: .5px;
  }
  .services-title .accent { color: var(--gold); }
  .services-list { list-style: none; margin-top: 8px; }
  .services-list li {
    font-size: 15px; font-weight: 500; color: var(--ink);
    height: 20.5px; display: flex; align-items: center; gap: 11px;
    white-space: nowrap;
  }
  .services-list li::before {
    content: ""; width: 8px; height: 8px; border-radius: 50%;
    background: var(--gold); flex: none;
  }
  .footer-company {
    position: absolute; left: 40px; top: 1068px; color: #fff;
  }
  .footer-company .name { color: var(--gold-light); font-weight: 600; font-size: 17px; }
  .footer-company .address { font-size: 14px; font-weight: 500; display: flex; align-items: center; gap: 8px; margin-top: 3px; }
  .footer-contact {
    position: absolute; right: 14px; top: 1020px;
    display: flex; gap: 14px; color: #fff; font-size: 12px; font-weight: 500;
  }
  .footer-contact span { display: flex; align-items: center; gap: 5px; white-space: nowrap; }
  .icon { width: 13px; height: 13px; fill: currentColor; flex: none; }
</style>
</head>
<body>
<main class="flyer">
  <svg class="flyer-art" width="800" height="1131" viewBox="0 0 800 1131">
    <defs>
      <linearGradient id="heroTone" x1="0" y1="0" x2="0" y2="1">
        <stop offset="0" stop-color="#d4d7dc"/>
        <stop offset=".4" stop-color="#a7adb6"/>
        <stop offset=".52" stop-color="#6c625a"/>
        <stop offset=".64" stop-color="#9a6a45"/>
        <stop offset="1" stop-color="#7c5034"/>
      </linearGradient>
      <linearGradient id="circleTruck" x1="0" y1="0" x2="0" y2="1">
        <stop offset="0" stop-color="#c9ccd3"/><stop offset=".5" stop-color="#3b3b3d"/><stop offset="1" stop-color="#a4683f"/>
      </linearGradient>
      <linearGradient id="circleSky" x1="0" y1="0" x2="0" y2="1">
        <stop offset="0" stop-color="#7f86c9"/><stop offset=".55" stop-color="#d9dde2"/><stop offset="1" stop-color="#a5683f"/>
      </linearGradient>
      <linearGradient id="circleGrader" x1="0" y1="0" x2="0" y2="1">
        <stop offset="0" stop-color="#7d8fd0"/><stop offset=".5" stop-color="#d0b24a"/><stop offset="1" stop-color="#b0673c"/>
      </linearGradient>
      <linearGradient id="circleTanker" x1="0" y1="0" x2="0" y2="1">
        <stop offset="0" stop-color="#b8c9dc"/><stop offset=".55" stop-color="#b59a7a"/><stop offset="1" stop-color="#8c5b38"/>
      </linearGradient>
      <linearGradient id="mascotTone" x1="0" y1="0" x2="0" y2="1">
        <stop offset="0" stop-color="#8cc8f5"/><stop offset="1" stop-color="#2f7fd6"/>
      </linearGradient>
    </defs>

    <rect class="hero-photo" role="img" aria-label="Photo of road train tipper trucks parked on red outback dirt under a cloudy sky" x="0" y="0" width="800" height="720" fill="url(#heroTone)"/>

    <path class="title-band" d="M0,565 C260,560 520,400 800,160 L800,440 C530,670 260,765 0,765 Z" fill="var(--charcoal)"/>
    <path class="paper-sweep" d="M0,765 C260,765 530,670 800,440 L800,1131 L0,1131 Z" fill="var(--paper)"/>
    <path class="gold-rule" d="M140,758 C320,745 450,690 560,620" stroke="var(--gold)" stroke-width="4" fill="none"/>
    <path class="gold-rule" d="M700,210 C730,190 760,170 790,148" stroke="var(--gold)" stroke-width="5" fill="none"/>

    <g class="photo-circles" stroke="#fff" stroke-width="8">
      <circle role="img" aria-label="Photo of a black prime mover truck on dirt" cx="600" cy="290" r="135" fill="url(#circleTruck)"/>
      <circle role="img" aria-label="Photo of a white and green road train truck" cx="730" cy="500" r="100" fill="url(#circleSky)"/>
      <circle role="img" aria-label="Photo of a yellow road grader on a dirt road" cx="570" cy="640" r="100" fill="url(#circleGrader)"/>
      <circle role="img" aria-label="Photo of a water tanker truck" cx="765" cy="715" r="85" fill="url(#circleTanker)"/>
    </g>

    <rect class="mascot" role="img" aria-label="Illustration of a water drop character drinking from a glass" x="640" y="840" width="105" height="105" rx="36" fill="url(#mascotTone)"/>

    <path class="footer-gold" d="M380,1055 C410,1055 415,1005 450,1005 L800,1005 L800,1055 Z" fill="var(--gold)"/>
    <path class="footer-dark" d="M0,1131 L0,1058 C300,1058 500,1056 800,1050 L800,1131 Z" fill="var(--charcoal-deep)"/>
  </svg>

  <div class="brand-mark">KVR</div>

  <h1 class="headline">KESTREL VALE<br>ROADWORKS</h1>

  <section class="services">
    <h2 class="services-title"><span class="accent">OUR</span> SERVICES</h2>
    <ul class="services-list">
      <li>Over size loads / Hot Shot Loads</li>
      <li>Heavy Vehicle Recovery services</li>
      <li>Potable Water Deliveries</li>
      <li>Road Building / Maintenance</li>
      <li>Earthworks</li>
      <li>Sand &amp; Metal Supply &amp; Cartage</li>
      <li>Road Train Tippers</li>
      <li>Road Train Tankers</li>
      <li>Road Train Flat Tops</li>
      <li>Drop Deck Trailers</li>
      <li>Mine site accredited equipment &amp; Operators.</li>
    </ul>
  </section>

  <div class="footer-contact">
    <span><svg class="icon" viewBox="0 0 24 24"><path d="M6.6 10.8a15.1 15.1 0 0 0 6.6 6.6l2.2-2.2a1 1 0 0 1 1-.25 11.4 11.4 0 0 0 3.6.57 1 1 0 0 1 1 1V20a1 1 0 0 1-1 1A17 17 0 0 1 3 4a1 1 0 0 1 1-1h3.5a1 1 0 0 1 1 1c0 1.25.2 2.45.57 3.57a1 1 0 0 1-.25 1z"/></svg>047 216 9381</span>
    <span><svg class="icon" viewBox="0 0 24 24"><path d="M2 5h20v14H2zm2 2v.4l8 5.1 8-5.1V7zm0 2.8V17h16V9.8l-8 5.1z"/></svg>darren@kestrelvaleroadworks.com.au</span>
  </div>

  <div class="footer-company">
    <div class="name">KVR Pty Ltd</div>
    <div class="address"><svg class="icon" viewBox="0 0 24 24" style="fill:var(--gold-light)"><path d="M12 3 2 12h3v8h5v-5h4v5h5v-8h3z"/></svg>Lot 514, Banksia Flats Track Coober Pedy</div>
  </div>
</main>
</body>
</html>
```